AI Business Tools Landing Page

My web-based website builder (Nurvanta.com) will be adding many new features in the very near future and I need an eye-catching landing page to promote these new products.

The page will have a primary section of the 8 main products we are promoting:
1. AI Instant Website Generator
2. AI Chatbot
3. Online Store Builder with AI Assistance
4. AI Auto-Blogging System
5. Online Scheduling System
6. Custom Email System
7. SEO Service
8. CRM System

The page will also have a smaller section for links to our affiliate programs. These can be smaller, less-promanent buttons or links. These are the affiliate products:
1. Get Your LLC
2. Website Design and Maintenance
3. Tavolin Ads Management
4. Social Media Posting Service
5. Logo Design
6. Trademark Registration
7. Patent Application
8. Printing Services (including postcards, flyers, and merch.)
9. Bulk AI Content Generator

The theme and color scheme of the page should follow the theme of our main website, which is https://nurvanta.com.

I need the page fully coded and ready to deploy on my server.

I look forward to seeing your amazing designs!

```html
<!DOCTYPE html>
<html lang="en">
<head>
<meta charset="utf-8">
<title>Nurvanta – The Premier AI Website Builder</title>
<link href="https://fonts.googleapis.com/css2?family=Inter:wght@400;500;600;700&display=swap" rel="stylesheet">
<style>
:root{
  --navy:#0a1a3f;
  --navy-deep:#071330;
  --hero-blue:#1e52c8;
  --btn-blue:#1f6bff;
  --accent:#1fa2ee;
  --heading:#2b3a5c;
  --body:#5b6680;
  --light-bg:#eaf1fa;
  --card-bg:#edf2fa;
  --white:#ffffff;
  --muted-num:#d6dbe4;
}
*{margin:0;padding:0;box-sizing:border-box}
html,body{width:1200px;height:2824px;overflow:hidden}
body{font-family:"Inter",sans-serif;background:var(--white);position:relative;color:var(--heading)}

/* Hero */
.hero{position:absolute;left:0;top:0;width:1200px;height:853px;overflow:hidden;
  background:radial-gradient(ellipse 700px 600px at 1100px 650px,#2460d8 0%,rgba(30,82,200,.6) 40%,rgba(10,26,63,0) 75%),
  linear-gradient(160deg,#15306f 0%,#0c1f4d 45%,var(--navy-deep) 80%);}
.nav{position:absolute;left:42px;top:0;width:1116px;height:114px;border-bottom:1px solid rgba(255,255,255,.15)}
.brand{position:absolute;left:0;top:40px;display:flex;align-items:center;gap:10px;color:var(--white);font-weight:600;font-size:26px}
.brand-mark{width:30px;height:30px;border-radius:50%;background:var(--accent)}
.nav-links{position:absolute;left:254px;top:47px;display:flex;gap:33px;color:rgba(255,255,255,.78);font-size:18px}
.nav-links span{display:flex;align-items:center;gap:6px}
.btn-login{position:absolute;left:848px;top:30px;width:106px;height:55px;border-radius:8px;background:var(--btn-blue);color:#fff;font-size:18px;display:flex;align-items:center;justify-content:center}
.btn-start{position:absolute;left:972px;top:30px;width:144px;height:55px;border-radius:8px;background:rgba(255,255,255,.12);color:rgba(255,255,255,.8);font-size:18px;display:flex;align-items:center;justify-content:center}
.hero-title{position:absolute;left:0;top:300px;width:1166px;text-align:center;font-size:84px;font-weight:700;letter-spacing:-2px;line-height:88px;
  background:linear-gradient(180deg,#ffffff 0%,#c5cfe4 100%);-webkit-background-clip:text;background-clip:text;color:transparent}
.hero-sub{position:absolute;left:0;top:503px;width:1166px;text-align:center;color:#e9eefa;font-size:20px}
.hero-input{position:absolute;left:234px;top:566px;width:438px;height:65px;border-radius:8px;background:rgba(255,255,255,.08);color:rgba(255,255,255,.5);font-size:20px;padding-left:37px;display:flex;align-items:center}
.hero-btn{position:absolute;left:690px;top:566px;width:243px;height:65px;border-radius:8px;background:var(--btn-blue);color:#fff;font-size:20px;display:flex;align-items:center;justify-content:center}

/* Products */
.products{position:absolute;left:0;top:853px;width:1200px;height:865px;background:var(--light-bg)}
.discover-title{position:absolute;left:83px;top:70px;font-size:42px;font-weight:600;line-height:49px;color:var(--heading);letter-spacing:-.5px}
.discover-title em{font-style:normal;color:var(--accent)}
.discover-text{position:absolute;left:627px;top:68px;width:500px;font-size:17px;line-height:30px;color:var(--body);letter-spacing:-.2px}
.rule{position:absolute;left:83px;top:272px;width:1034px;height:2px;background:#d3deed}
.feature-art{position:absolute;left:420px;top:340px;width:380px;height:400px;border-radius:40px;
  background:radial-gradient(ellipse at 50% 55%,rgba(120,190,240,.55) 0%,rgba(160,210,245,.3) 45%,rgba(234,241,250,0) 72%)}
.product{position:absolute;background:var(--white);border-radius:8px;box-shadow:0 10px 30px rgba(40,80,140,.12);display:flex;align-items:center;padding-left:29px}
.product .num{width:40px;height:40px;border-radius:50%;background:var(--muted-num);color:#fff;font-size:24px;font-weight:500;display:flex;align-items:center;justify-content:center;flex:none}
.product .name{margin-left:26px;color:var(--accent);font-size:19.5px;font-weight:500;line-height:28px}

/* Why */
.why-glow{position:absolute;left:300px;top:1718px;width:600px;height:130px;background:radial-gradient(ellipse at 50% 0%,rgba(120,190,240,.4),rgba(255,255,255,0) 70%)}
.why-title{position:absolute;left:0;top:1828px;width:1200px;text-align:center;font-size:42px;font-weight:600;line-height:50px;color:var(--heading);letter-spacing:-.5px}
.why-text{position:absolute;left:0;top:1947px;width:1200px;text-align:center;font-size:17.5px;line-height:30px;color:var(--body)}
.feature{position:absolute;width:506px;height:298px;background:var(--card-bg);border-radius:10px;text-align:center}
.feature h3{position:absolute;left:0;top:108px;width:100%;font-size:23.5px;font-weight:600;color:var(--heading)}
.feature p{position:absolute;left:55px;top:155px;width:400px;text-align:left;font-size:15.5px;line-height:27.5px;color:var(--body);letter-spacing:-.15px}
.feature .icon{position:absolute;left:197px;top:-32px}
</style>
</head>
<body>

<header class="hero">
  <nav class="nav">
    <div class="brand"><span class="brand-mark"></span>Nurvanta</div>
    <div class="nav-links">
      <span>Services <svg width="14" height="9" viewBox="0 0 14 9"><path d="M1 1l6 6 6-6" stroke="currentColor" stroke-width="1.8" fill="none"/></svg></span>
      <span>Products <svg width="14" height="9" viewBox="0 0 14 9"><path d="M1 1l6 6 6-6" stroke="currentColor" stroke-width="1.8" fill="none"/></svg></span>
      <span>Pricing</span>
      <span>About Us</span>
      <span>Make Money</span>
    </div>
    <a class="btn-login">Log in</a>
    <a class="btn-start">Start for free</a>
  </nav>
  <h1 class="hero-title">The Premier<br>AI Website Builder</h1>
  <p class="hero-sub">Your free stunning website in one click built by Artificial Intelligence</p>
  <div class="hero-input">Enter your business name</div>
  <a class="hero-btn">Build my website</a>
</header>

<section class="products">
  <h2 class="discover-title">Discover the Future of<br>Website Creation with<br><em>Nurvanta</em></h2>
  <p class="discover-text">In the rapidly evolving digital era, the integration of Artificial Intelligence (AI) into various sectors is unmistakably transformative. Website creation, a domain once dominated by manual coding and design intricacies, is now witnessing a groundbreaking revolution, thanks to AI technology.</p>
  <div class="rule"></div>
  <div class="feature-art" role="img" aria-label="Illustration of the platform connected to a website design page"></div>

  <div class="product" style="left:83px;top:343px;width:384px;height:87px"><span class="num">1</span><span class="name">AI Instant Website Generator</span></div>
  <div class="product" style="left:83px;top:461px;width:222px;height:88px"><span class="num">2</span><span class="name">AI ChatBot</span></div>
  <div class="product" style="left:83px;top:579px;width:428px;height:92px"><span class="num">3</span><span class="name">Online Store Builder<br>(E-Commerce) with AI Assistance</span></div>
  <div class="product" style="left:83px;top:701px;width:351px;height:88px"><span class="num">4</span><span class="name">AI Auto-Blogging System</span></div>

  <div class="product" style="left:690px;top:343px;width:360px;height:87px"><span class="num">5</span><span class="name">Online Scheduling System</span></div>
  <div class="product" style="left:690px;top:461px;width:427px;height:88px"><span class="num">6</span><span class="name">Custom emails using your domain</span></div>
  <div class="product" style="left:690px;top:579px;width:365px;height:92px"><span class="num">7</span><span class="name">SEO Service – Automatic<br>Backlink Building</span></div>
  <div class="product" style="left:690px;top:701px;width:425px;height:92px"><span class="num">8</span><span class="name">Customer Relationship<br>Management (CRM) System</span></div>
</section>

<div class="why-glow"></div>
<h2 class="why-title">Why Choose Nurvanta for Your<br>Website Creation?</h2>
<p class="why-text">Nurvanta leverages AI technology to streamline the website creation<br>process, making it faster, more efficient, and incredibly user-friendly.<br>Here's what sets Nurvanta apart:</p>

<div class="feature" style="left:83px;top:2119px">
  <svg class="icon" width="112" height="112" viewBox="0 0 112 112"><circle cx="56" cy="56" r="54" fill="#fff" stroke="#0f2540" stroke-width="3"/><circle cx="56" cy="56" r="42" fill="none" stroke="#9fd3f5" stroke-width="1.5"/><circle cx="56" cy="56" r="26" fill="#0f2540"/><rect x="44" y="47" width="24" height="18" rx="2" fill="none" stroke="#fff" stroke-width="1.6"/><path d="M46 62l6-7 5 5 4-3 5 5" stroke="#fff" stroke-width="1.4" fill="none"/></svg>
  <h3>Unparalleled Flexibility</h3>
  <p>Customize your site with ease, adding custom images, content, and more to truly make it your own.</p>
</div>
<div class="feature" style="left:610px;top:2119px">
  <svg class="icon" width="112" height="112" viewBox="0 0 112 112"><circle cx="56" cy="56" r="54" fill="#fff" stroke="#1fa2ee" stroke-width="3"/><circle cx="56" cy="56" r="42" fill="none" stroke="#9fd3f5" stroke-width="1.5"/><circle cx="56" cy="56" r="26" fill="#1fa2ee"/><rect x="43" y="45" width="26" height="18" rx="2" fill="none" stroke="#fff" stroke-width="1.6"/><path d="M52 68h8M56 63v5" stroke="#fff" stroke-width="1.6"/></svg>
  <h3>Mobile Optimization</h3>
  <p>Nurvanta ensures your website is beautifully rendered on PCs, smartphones, and tablets, offering a seamless user experience across all devices.</p>
</div>
<div class="feature" style="left:83px;top:2467px">
  <svg class="icon" width="112" height="112" viewBox="0 0 112 112"><circle cx="56" cy="56" r="54" fill="#fff" stroke="#1fa2ee" stroke-width="3"/><circle cx="56" cy="56" r="42" fill="none" stroke="#9fd3f5" stroke-width="1.5"/><circle cx="56" cy="56" r="26" fill="#1fa2ee"/><rect x="45" y="45" width="22" height="22" rx="2" fill="none" stroke="#fff" stroke-width="1.6"/><circle cx="56" cy="53" r="4" fill="none" stroke="#fff" stroke-width="1.4"/><path d="M50 61h12M50 64h12" stroke="#fff" stroke-width="1.4"/></svg>
  <h3>Zero Cost to Start</h3>
  <p>Dive into the world of website creation without any initial investment. Nurvanta offers a free platform to build your website, providing a cost-effective solution for businesses and individuals alike.</p>
</div>
<div class="feature" style="left:610px;top:2467px">
  <svg class="icon" width="112" height="112" viewBox="0 0 112 112"><circle cx="56" cy="56" r="54" fill="#fff" stroke="#0f2540" stroke-width="3"/><circle cx="56" cy="56" r="42" fill="none" stroke="#9fd3f5" stroke-width="1.5"/><circle cx="56" cy="56" r="26" fill="#0f2540"/><circle cx="56" cy="57" r="10" fill="none" stroke="#fff" stroke-width="1.5"/><path d="M46 57h20M56 47c-5 6-5 14 0 20M56 47c5 6 5 14 0 20" stroke="#fff" stroke-width="1.3" fill="none"/></svg>
  <h3>Robust Cloud Infrastructure</h3>
  <p>Benefit from a secure, high-powered cloud computing environment that guarantees reliability and speed for all Nurvanta websites.</p>
</div>

</body>
</html>
```